Soho based IT support firm flyer.

We need a flyer to boost our business. We're a tech support firm based in Soho, London and provide helpdesk and call out support to SMEs in and around London.
They'll be two flyers with the same design. One is location specific and has the copy:
-
1 Month Free IT Support!
Based in Soho, we provide expert tech support for both Zelks and PCs.
We have monthly as well as pay-as-you-go plans to fit your business.
Call us now and we'll show you how we can save you up to 50% on your IT spend.
-None location based is-
1 Month Free IT Support!
We provide expert, professional tech support for both Zelks and PCs.
• Dedicated full time helpdesk
• Same day onsite visits
• Proactive support with monitoring
• 98% satisfaction score*
*taken from satisfaction survey sent out on closure of every case for Oct 2011 to Oct 2012
-
The location one needs to include a map with our location marked as postcode Q9X 4TT.
I'm fine with royalty photos being used within a reasonable price. Please use PicturVault.
Our site shows our brand best. Please keep as close to this as possible.
http://brivo-desk.example
Thanks for looking.

```html
<!DOCTYPE html>
<html lang="en">
<head>
<meta charset="utf-8">
<title>Brivo Desk flyers</title>
<link rel="stylesheet" href="https://fonts.googleapis.com/css2?family=Open+Sans:wght@400;600;700&display=swap">
<style>
:root{
  --stage:#e9e6df;
  --card:#f7f7f1;
  --card-low:#e3efc4;
  --leaf-dark:#2f4a22;
  --leaf-mid:#5f8a36;
  --leaf-light:#a9c96a;
  --bar:#cfe18f;
  --bar-edge:#b7cf6e;
  --bar-text:#5b6b2a;
  --orange:#f39a1f;
  --orange-deep:#e8860f;
  --green-box:#bcd76b;
  --green-text:#3f5a1a;
  --white:#ffffff;
  --red:#e32222;
  --title-box:rgba(20,30,18,.72);
}
*{margin:0;padding:0;box-sizing:border-box}
html,body{width:1200px;height:452px;overflow:hidden;background:var(--stage)}
body{position:relative;font-family:"Open Sans",Arial,sans-serif}
.flyer{position:absolute;top:46px;width:516px;height:358px;background:linear-gradient(180deg,var(--card) 55%,var(--card-low) 100%);box-shadow:0 2px 6px rgba(0,0,0,.25);overflow:hidden}
.flyer--location{left:50px}
.flyer--general{left:636px}
.header-photo{position:absolute;left:0;top:0;width:100%;height:92px;background:radial-gradient(ellipse at 50% 60%,var(--leaf-light) 0%,var(--leaf-mid) 40%,var(--leaf-dark) 100%)}
.headline{position:absolute;left:14px;top:12px;width:488px;height:62px;background:var(--title-box);color:var(--white);font-weight:600;font-size:35px;line-height:62px;text-align:center;letter-spacing:-.3px;white-space:nowrap}
.headline b{font-weight:700;font-size:38px}
.copy-bar{position:absolute;left:16px;width:482px;height:23px;background:var(--bar);border:1px solid var(--bar-edge);border-radius:4px;box-shadow:1px 2px 2px rgba(0,0,0,.18);color:var(--bar-text);font-size:12.2px;line-height:21px;text-align:center;white-space:nowrap}
.copy-bar:nth-of-type(1){top:101px}
.copy-bar:nth-of-type(2){top:134px}
.copy-bar:nth-of-type(3){top:166px}
.address{position:absolute;left:18px;top:198px;width:172px;height:78px;background:var(--orange);color:var(--white);font-size:15px;line-height:18px;padding:5px 8px;font-style:normal;white-space:nowrap}
.address-arrow{position:absolute;left:188px;top:184px;width:54px;height:106px}
.map{position:absolute;left:238px;top:194px;width:258px;height:156px;border:4px solid var(--orange);background:linear-gradient(135deg,#eceae2 0%,#dcdcd2 55%,#f2d98a 100%)}
.contact{position:absolute;left:18px;top:290px;width:212px;height:58px;background:var(--green-box);color:var(--green-text);font-weight:700;font-size:15px;line-height:24px;padding:4px 7px;white-space:nowrap;letter-spacing:-.2px}
.contact .phone{display:flex;align-items:center;gap:6px;font-size:19px;letter-spacing:0}
.contact .phone svg{width:22px;height:18px;flex:none}
.benefits{position:absolute;left:0;top:194px;width:100%;height:102px;background:linear-gradient(90deg,var(--orange-deep),var(--orange));color:var(--white);font-family:Arial,Helvetica,sans-serif;font-weight:700;font-size:18.5px;line-height:23px;list-style:none;padding:6px 0 0;text-align:center;white-space:nowrap}
.benefits li{padding-right:60px}
.benefits .mark{color:var(--red)}
.footnote{position:absolute;left:14px;top:306px;width:272px;color:var(--red);font-family:Arial,Helvetica,sans-serif;font-size:11.4px;line-height:17px}
.contact--orange{left:290px;top:296px;width:214px;height:56px;background:var(--orange);color:var(--white);border-radius:3px}
</style>
</head>
<body>

<section class="flyer flyer--location">
  <div class="header-photo" role="img" aria-label="Blurred green foliage photograph"></div>
  <h1 class="headline"><b>1</b> Month Free IT Support!</h1>
  <p class="copy-bar">Based in Soho, we provide expert tech support for both Zelks and PCs.</p>
  <p class="copy-bar">We have monthly as well as pay-as-you-go plans to fit your business.</p>
  <p class="copy-bar">Call us now and we'll show you how we can save you up to 50% on your IT spend.</p>
  <address class="address">12-14 Marlow House<br>Kestrel Street<br>London<br>Q9X 4TT</address>
  <svg class="address-arrow" viewBox="0 0 54 106" aria-hidden="true"><polygon points="0,22 4,22 4,0 54,53 4,106 4,84 0,84" fill="#f39a1f"/></svg>
  <div class="map" role="img" aria-label="Street map of Soho with the office location marked"></div>
  <div class="contact">
    <div class="phone"><svg viewBox="0 0 22 18" aria-hidden="true"><path d="M1 6c0-3 4-5 10-5s10 2 10 5v2h-5V5.5c-1.5-.6-3-.8-5-.8s-3.5.2-5 .8V8H1z" fill="currentColor"/><path d="M4 10h14l2 7H2z" fill="currentColor"/></svg>0203 555 0147</div>
    <div>www.brivo-desk.example</div>
  </div>
</section>

<section class="flyer flyer--general">
  <div class="header-photo" role="img" aria-label="Blurred green foliage photograph"></div>
  <h1 class="headline"><b>1</b> Month Free IT Support!</h1>
  <p class="copy-bar">We provide expert, professional tech support for both Zelks and PCs.</p>
  <p class="copy-bar">We have monthly as well as pay-as-you-go plans to fit your business.</p>
  <p class="copy-bar">Call us now and we'll show you how we can save you up to 50% on your IT spend.</p>
  <ul class="benefits">
    <li>• Dedicated full time helpdesk</li>
    <li>• Same day onsite visits</li>
    <li>• Proactive support with monitoring</li>
    <li>• 98% satisfaction score<span class="mark">*</span></li>
  </ul>
  <p class="footnote">*taken from satisfaction survey sent out on closure of every case for Oct 2011 to Oct 2012</p>
  <div class="contact contact--orange">
    <div class="phone"><svg viewBox="0 0 22 18" aria-hidden="true"><path d="M1 6c0-3 4-5 10-5s10 2 10 5v2h-5V5.5c-1.5-.6-3-.8-5-.8s-3.5.2-5 .8V8H1z" fill="currentColor"/><path d="M4 10h14l2 7H2z" fill="currentColor"/></svg>0203 555 0147</div>
    <div>www.brivo-desk.example</div>
  </div>
</section>

</body>
</html>
```